New App: 4 Page Design - Updated Brief

We need an indicative design for our new app 'Bolt Haul', a delivery service for tools and hardware in Sydney, Australia.

Imagine a service which copies the blue print of Ferro Meals, but for tools and Hardware. Where builders and tradespeople are stuck on-site at work and need a tool to be delivered to them on-site, same day. They can jump onto this app and in-put their address, then select an item from the catalogue and confirm the order. Once the order has been collected and due for delivery a map will show the location of the delivery driver.

We'd like 4 pages designed.

1st page) Loading page, similar to but not the same as the FerroMeals example attached.

2nd page) Home page - featuring the logo and some icons which direct users around the website. (Please see link to design example: https://www.ferromeals-example.com/au?ref_id=aa11bb22-c333-4d44-85e5-ff66aa77bb88 )

3rd page) A page which depicts the catalogue of tools and hardware (showing generic tools available (Please see link to design example https://www.kelmtrade-example.com.au/products/building-hardware).

4th page) We'd like a page which shows a map, tracking the delivery, from the hardware store, to the location of the purchaser, exactly like any typical ferro delivery service.

Please see the below website for design guidance and ideas

https://www.kelmtrade-example.com.au/?src=xx.yy&tid=Zq4RtL8mNw2PvX6sKd0HfJ3bYc9GuE7aTo1LiVn5MeWx_xyz

Target Market(s)

Construction industry, tradespeople

Industry/Entity Type

Construction and Tradesmen

Colors

Designer to choose colors to be used in the design.

Requirements
Must have
• Desired Colour schemes: up to the designer but no bright colours
Nice to have
• An icon bar at the bottom of the page that directs you to the various pages on the app. Example shown in the attachments
Should not have
• An exact copy of the Ferro App

```html
<!DOCTYPE html>
<html lang="en">
<head>
<meta charset="utf-8">
<title>Bolt Haul – Get started</title>
<link rel="stylesheet" href="https://fonts.googleapis.com/css2?family=Inter:wght@600;700&display=swap">
<style>
  :root {
    --teal: #0e5258;
    --white: #ffffff;
  }
  html, body {
    margin: 0;
    padding: 0;
    width: 1200px;
    height: 2597px;
    overflow: hidden;
    background: var(--teal);
    font-family: "Inter", Arial, sans-serif;
  }
  .screen {
    position: relative;
    width: 1200px;
    height: 2597px;
  }
  .service-grid {
    position: absolute;
    left: 104px;
    top: 190px;
    display: grid;
    grid-template-columns: repeat(3, 295px);
    grid-auto-rows: 295px;
    gap: 47px;
    margin: 0;
    padding: 0;
    list-style: none;
  }
  .service-tile {
    width: 295px;
    height: 295px;
    border-radius: 50%;
    background: var(--white);
    display: flex;
    align-items: center;
    justify-content: center;
  }
  .service-icon {
    width: 112px;
    height: 112px;
    fill: none;
    stroke: var(--teal);
    stroke-width: 5;
    stroke-linecap: round;
    stroke-linejoin: round;
  }
  .brand-name {
    color: var(--teal);
    font-weight: 700;
    font-size: 50px;
    line-height: 1.05;
    text-align: center;
  }
  .headline {
    position: absolute;
    left: 105px;
    top: 2010px;
    margin: 0;
    color: var(--white);
    font-weight: 600;
    font-size: 89px;
    letter-spacing: -1.5px;
    white-space: nowrap;
  }
  .cta-button {
    position: absolute;
    left: 105px;
    top: 2178px;
    width: 978px;
    height: 246px;
    border-radius: 12px;
    background: var(--white);
    color: var(--teal);
    text-decoration: none;
    display: flex;
    align-items: center;
    justify-content: center;
    font-weight: 700;
    font-size: 58px;
    letter-spacing: 2px;
  }
  .cta-arrow {
    position: absolute;
    right: 100px;
    top: 96px;
    width: 56px;
    height: 54px;
    fill: none;
    stroke: var(--teal);
    stroke-width: 7;
    stroke-linecap: round;
    stroke-linejoin: round;
  }
</style>
</head>
<body>
<main class="screen">
  <ul class="service-grid">
    <li class="service-tile"><span class="brand-name">Bolt<br>Haul</span></li>

    <li class="service-tile" aria-label="Plumbing">
      <svg class="service-icon" viewBox="0 0 100 100"><path d="M14 55h72v10a12 12 0 0 1-12 12H26a12 12 0 0 1-12-12z"/><path d="M28 77l-3 7M72 77l3 7"/><path d="M62 55V28a10 10 0 0 1 20 0v4"/><path d="M74 34h16v8H74z"/><path d="M78 46v4M86 46v4"/></svg>
    </li>
    <li class="service-tile" aria-label="Repairs">
      <svg class="service-icon" viewBox="0 0 100 100"><path d="M22 14a14 14 0 0 0 8 26l32 32a14 14 0 1 0 10-10L40 30a14 14 0 0 0-26-8l10 10-2 6-6 2z"/></svg>
    </li>

    <li class="service-tile" aria-label="Cleaning">
      <svg class="service-icon" viewBox="0 0 100 100"><path d="M40 10v50"/><path d="M30 60h20l8 26H22z"/><path d="M30 72v14M40 72v14M50 72v14"/><path d="M62 38v14M55 45h14M74 56v14M67 63h14"/></svg>
    </li>
    <li class="service-tile" aria-label="Smart home">
      <svg class="service-icon" viewBox="0 0 100 100"><path d="M12 48L50 18l38 30"/><path d="M22 42v38h56V42"/><path d="M36 60a20 20 0 0 1 28 0M42 66a11 11 0 0 1 16 0"/><circle cx="50" cy="72" r="2"/></svg>
    </li>
    <li class="service-tile" aria-label="Painting">
      <svg class="service-icon" viewBox="0 0 100 100"><rect x="22" y="14" width="54" height="18" rx="4"/><path d="M76 23h6v20H46v12"/><rect x="41" y="55" width="10" height="30" rx="3"/></svg>
    </li>

    <li class="service-tile" aria-label="Outdoor">
      <svg class="service-icon" viewBox="0 0 100 100"><circle cx="44" cy="32" r="8"/><path d="M44 14v6M44 44v6M26 32h6M56 32h6M31 19l4 4M53 41l4 4M31 45l4-4M53 23l4-4"/><path d="M12 68h50l22-18"/><path d="M12 80h54M20 68v12M58 68v12"/></svg>
    </li>
    <li class="service-tile" aria-label="Lighting">
      <svg class="service-icon" viewBox="0 0 100 100"><path d="M38 70c0-12-14-18-14-36a26 26 0 0 1 52 0c0 18-14 24-14 36z"/><path d="M38 78h24M40 86h20"/><path d="M58 24a10 10 0 0 1 6 8"/></svg>
    </li>
    <li class="service-tile" aria-label="Cabinetry">
      <svg class="service-icon" viewBox="0 0 100 100"><rect x="10" y="36" width="80" height="38"/><path d="M50 36v38M14 74v8M86 74v8"/><path d="M38 50v10M62 50v10"/><path d="M68 36V26a6 6 0 0 1 12 0"/></svg>
    </li>

    <li class="service-tile" aria-label="Furniture">
      <svg class="service-icon" viewBox="0 0 100 100"><path d="M26 48V36a10 10 0 0 1 10-10h28a10 10 0 0 1 10 10v12"/><path d="M18 48a7 7 0 0 1 8 7v5h48v-5a7 7 0 1 1 8 7v10H18V62a7 7 0 0 1 0-14z"/><path d="M24 72v6M76 72v6"/></svg>
    </li>
    <li class="service-tile" aria-label="Trailer hire">
      <svg class="service-icon" viewBox="0 0 100 100"><path d="M10 60h20"/><path d="M30 60V44h54v16z"/><circle cx="56" cy="62" r="7"/><path d="M30 52h54"/></svg>
    </li>
    <li class="service-tile" aria-label="Garden">
      <svg class="service-icon" viewBox="0 0 100 100"><path d="M50 88V60C22 58 14 36 18 12c26 2 40 20 32 48"/><path d="M26 22l24 38"/><path d="M50 70c4-16 18-22 34-20-2 16-14 22-34 20z"/><path d="M58 66l22-14"/></svg>
    </li>

    <li class="service-tile" aria-label="Flooring">
      <svg class="service-icon" viewBox="0 0 100 100"><path d="M30 38l24-24a12 12 0 0 1 18 18L48 56"/><circle cx="26" cy="58" r="14"/><circle cx="26" cy="58" r="5"/><path d="M36 48l40-16M16 72l26 14 40-46"/><path d="M50 80l4 4M58 72l4 4M66 62l4 4"/></svg>
    </li>
    <li class="service-tile" aria-label="Blinds">
      <svg class="service-icon" viewBox="0 0 100 100"><path d="M18 12h66M18 24h62M18 36h62M18 48h62M18 60h62M18 72h62"/><path d="M80 12v68"/><path d="M74 80h12v10H74z"/></svg>
    </li>
    <li class="service-tile" aria-label="Bricklaying">
      <svg class="service-icon" viewBox="0 0 100 100"><path d="M16 18l10-8 24 24-8 8z"/><path d="M46 42l10 12"/><path d="M56 54l30 30-36-6z"/></svg>
    </li>
  </ul>

  <h1 class="headline">Get start with Bolt Haul</h1>

  <a class="cta-button" href="#">
    GO TO WEBSITE
    <svg class="cta-arrow" viewBox="0 0 56 54"><path d="M4 27h46M28 5l22 22-22 22"/></svg>
  </a>
</main>
</body>
</html>
```